Ayurvedic Beauty Company in Need of Business Cards

My company is a high-end ayurvedic beauty brand. I need a business card that represents that. The designer should utilize logo and color palette. I want these cards to be printed with the foil accents so keep that in mind.

I have attached the ai of my logo and business card info. As well as, some of the product we are launching soon, they do not have to be on the card.

Be creative and have fun.

Thanks in advance,

Marla

```html
<!DOCTYPE html>
<html lang="en">
<head>
<meta charset="utf-8">
<title>Saffron Bloom — Business Card</title>
<link rel="stylesheet" href="https://fonts.googleapis.com/css2?family=Open+Sans:wght@400;600;700&display=swap">
<style>
  :root {
    --backdrop: #efe7dc;
    --card-light: #dcb88c;
    --card-mid: #c99c69;
    --card-dark: #b88a5a;
    --ink: #141414;
    --rule: #2a2118;
    --foil-text: #7a5a30;
    --foil-hi: #f3e2bb;
    --foil-lo: #8a6334;
    --foil-mid: #c9a067;
  }
  * { margin: 0; padding: 0; box-sizing: border-box; }
  html, body { width: 1200px; height: 900px; overflow: hidden; }
  body {
    position: relative;
    background: var(--backdrop);
    font-family: "Open Sans", Arial, sans-serif;
    color: var(--ink);
  }
  .card {
    position: absolute;
    width: 556px;
    height: 343px;
    background: linear-gradient(160deg, var(--card-light) 0%, var(--card-mid) 55%, var(--card-dark) 100%);
    box-shadow: 2px 3px 6px rgba(0, 0, 0, 0.35);
  }
  .card--front { left: 330px; top: 90px; }
  .card--back { left: 330px; top: 469px; }

  .holder {
    position: absolute;
    top: 88px;
    left: 0;
    width: 100%;
    text-align: center;
  }
  .holder__name {
    font-size: 20px;
    font-weight: 600;
    letter-spacing: 0.3px;
    line-height: 26px;
  }
  .holder__title {
    font-size: 15px;
    line-height: 18px;
  }
  .holder__rule {
    width: 179px;
    height: 1px;
    margin: 15px auto 0;
    background: var(--rule);
  }
  .contact {
    list-style: none;
    margin-top: 17px;
    font-size: 15px;
    line-height: 20px;
  }
  .contact__label { font-weight: 700; }

  .brand {
    position: absolute;
    inset: 0;
  }
  .brand__disc {
    position: absolute;
    left: 184px;
    top: 58px;
    width: 190px;
    height: 190px;
    border-radius: 50%;
    background: linear-gradient(135deg,
      var(--foil-hi) 0%,
      var(--foil-mid) 28%,
      var(--foil-lo) 48%,
      var(--foil-hi) 68%,
      var(--foil-mid) 84%,
      var(--foil-lo) 100%);
    box-shadow: 1px 2px 3px rgba(60, 40, 15, 0.45);
  }
  .brand__name {
    position: absolute;
    left: 0;
    top: 262px;
    width: 100%;
    text-align: center;
    font-size: 25px;
    font-weight: 700;
    letter-spacing: 1px;
    color: var(--foil-text);
  }
</style>
</head>
<body>
  <section class="card card--front" aria-label="Card front">
    <div class="holder">
      <h1 class="holder__name">MARLA DEVANE</h1>
      <p class="holder__title">CEO</p>
      <div class="holder__rule"></div>
      <ul class="contact">
        <li><span class="contact__label">P:</span> 1(888) 555-0142</li>
        <li><span class="contact__label">M:</span> 1(347) 555-0186</li>
        <li><span class="contact__label">E:</span> marla@lovesaffronbloom.com</li>
        <li><span class="contact__label">W:</span> www.lovesaffronbloom.com</li>
      </ul>
    </div>
  </section>

  <section class="card card--back" aria-label="Card back">
    <div class="brand">
      <div class="brand__disc" role="img" aria-label="Gold foil brand mark"></div>
      <p class="brand__name">SAFFRON BLOOM</p>
    </div>
  </section>
</body>
</html>
```